Lawn mowing business card design

We need a business card design for our lawn mowing and gardening business which is located in the Northern Beaches of Sydney. Our business name is Meadowline Turf and our logo is predominantly green and yellow in color. Please see our website at www.meadowlineturf.com.au for design ideas. The business targets young professionals and older clientele. As such the font should be easy to read, but I also want the business card to be colorful and stand out.

Target Market(s)

young professionals

Industry/Entity Type

Lawn Care

Contact Information for Business Card

Meadowline Turf, Gareth Pellow, 0478559201, www.meadowlineturf.com.au, email: meadowlineturf@mailbox-example.com

Font styles to use
Serif

Colors
9bcb3b
fbed22

Requirements
Must have
• Must include the details listed above. Must include the attached logo.
Nice to have
• Logo attached with two copies. The logo without any writing is high quality, please feel free to be creative with the text stating our business name "Meadowline Turf" using this file.

```html
<!DOCTYPE html>
<html lang="en">
<head>
<meta charset="utf-8">
<title>Meadowline Turf – Business Card</title>
<link href="https://fonts.googleapis.com/css2?family=PT+Sans:wght@400;700&display=swap" rel="stylesheet">
<style>
  :root {
    --page: #e4e4e2;
    --sky-top: #9ec3e8;
    --sky-mid: #d9e8f5;
    --sky-low: #ffffff;
    --grass-light: #9bcb3b;
    --grass-dark: #3f9a2a;
    --soil: #4a3526;
    --soil-light: #6a5444;
    --name-green: #1e8a3e;
    --name-dark: #4a3526;
    --accent-yellow: #fbed22;
    --icon-yellow: #e9b815;
    --text-light: #f4efe9;
  }
  * { box-sizing: border-box; margin: 0; padding: 0; }
  html, body { width: 1200px; height: 1106px; overflow: hidden; }
  body {
    background: var(--page);
    font-family: "PT Sans", sans-serif;
    display: flex;
    flex-direction: column;
    align-items: center;
    justify-content: center;
    gap: 40px;
  }
  .card {
    position: relative;
    width: 820px;
    height: 500px;
    border-radius: 26px;
    overflow: hidden;
    box-shadow: 0 6px 18px rgba(0,0,0,0.18);
    background: var(--soil);
  }
  .card__sky {
    position: absolute; left: 0; top: 0; width: 100%; height: 300px;
    background: linear-gradient(200deg, var(--sky-top) 0%, var(--sky-mid) 45%, var(--sky-low) 85%);
  }
  .card__grass {
    position: absolute; left: 0; top: 248px; width: 100%; height: 56px;
    background: linear-gradient(180deg, rgba(155,203,59,0) 0%, var(--grass-light) 35%, var(--grass-dark) 100%);
  }
  .card__soil {
    position: absolute; left: 0; top: 300px; width: 100%; height: 200px;
    background: linear-gradient(160deg, var(--soil-light) 0%, var(--soil) 55%, #3b2a1e 100%);
  }
  .brand {
    position: absolute;
    display: flex; align-items: center; gap: 14px;
    color: var(--name-green);
    font-weight: 700;
  }
  .brand__dot {
    border-radius: 50%;
    background: var(--accent-yellow);
    flex: none;
  }
  .card--front .brand { left: 48px; top: 150px; font-size: 34px; }
  .card--front .brand__dot { width: 34px; height: 34px; }
  .card--back .brand { left: 150px; top: 150px; font-size: 56px; }
  .card--back .brand__dot { width: 56px; height: 56px; }
  .person {
    position: absolute; right: 56px; top: 190px;
    font-size: 40px; letter-spacing: 1px; text-transform: uppercase;
  }
  .person__first { color: var(--name-green); }
  .person__last { color: var(--name-dark); }
  .contact {
    position: absolute; color: var(--text-light);
    font-size: 30px; display: flex; align-items: center; gap: 16px;
  }
  .contact svg { width: 24px; height: 24px; flex: none; }
  .contact--phone { left: 40px; top: 400px; }
  .contact--mail { left: 330px; top: 336px; }
  .contact--web { left: 330px; top: 410px; }
  .card--back .contact--web { left: auto; right: 60px; top: 380px; font-size: 34px; }
</style>
</head>
<body>

<section class="card card--front" aria-label="Business card front">
  <div class="card__sky" role="img" aria-label="Soft blue sky with light clouds"></div>
  <div class="card__soil"></div>
  <div class="card__grass" role="img" aria-label="Strip of green grass with small daisies"></div>
  <div class="brand"><span class="brand__dot"></span>Meadowline Turf</div>
  <div class="person"><span class="person__first">Gareth</span> <span class="person__last">Pellow</span></div>
  <div class="contact contact--phone">
    <svg viewBox="0 0 24 24"><path fill="var(--icon-yellow)" d="M6.6 10.8a15 15 0 0 0 6.6 6.6l2.2-2.2c.3-.3.7-.4 1-.2 1.1.4 2.3.6 3.6.6.6 0 1 .4 1 1V20c0 .6-.4 1-1 1A17 17 0 0 1 3 4c0-.6.4-1 1-1h3.5c.6 0 1 .4 1 1 0 1.3.2 2.5.6 3.6.1.3 0 .7-.2 1z"/></svg>
    0478559201
  </div>
  <div class="contact contact--mail">
    <svg viewBox="0 0 24 24"><rect x="2" y="5" width="20" height="14" rx="1" fill="var(--icon-yellow)"/><path d="M2 6l10 7 10-7" fill="none" stroke="var(--soil)" stroke-width="1.6"/></svg>
    meadowlineturf@mailbox-example.com
  </div>
  <div class="contact contact--web">
    <svg viewBox="0 0 24 24"><circle cx="12" cy="12" r="10" fill="var(--icon-yellow)"/><path d="M2 12h20M12 2c3 3 3 17 0 20M12 2c-3 3-3 17 0 20" fill="none" stroke="var(--soil)" stroke-width="1.2"/></svg>
    www.meadowlineturf.com.au
  </div>
</section>

<section class="card card--back" aria-label="Business card back">
  <div class="card__sky" role="img" aria-label="Soft blue sky with light clouds"></div>
  <div class="card__soil"></div>
  <div class="card__grass" role="img" aria-label="Strip of green grass with small daisies"></div>
  <div class="brand"><span class="brand__dot"></span>Meadowline Turf</div>
  <div class="contact contact--web">
    <svg viewBox="0 0 24 24"><circle cx="12" cy="12" r="10" fill="var(--icon-yellow)"/><path d="M2 12h20M12 2c3 3 3 17 0 20M12 2c-3 3-3 17 0 20" fill="none" stroke="var(--soil)" stroke-width="1.2"/></svg>
    www.meadowlineturf.com.au
  </div>
</section>

</body>
</html>
```